Killer business card for bowling event and marketing company

Rolling T Ventures is a sports marketing company that specializes in unique bowling events that provide return on investment for sponsors and memorable experiences for participants and spectators. We need a new business card that simultaneously communicates professionalism and fun. Our preferred colors are black and re

Target Market(s)

Executives in the marketing and sponsorship departments of companies, tourism executives, bowling center owners, and people who love to bowl.

Industry/Entity Type

Business

Contact Information for Business Card

Neil T Farrow
Rolling T Ventures
PO Box 47
Alder Falls, Vermont USA 00000
Email: neilt@rollingtventures.example
Mobile: 1-555-318-4762

Requirements
Must have
• Our preferred colors are black and red.
Nice to have
• I am considering the use of the attached image for the back of the card.

```html
<!DOCTYPE html>
<html lang="en">
<head>
<meta charset="utf-8">
<title>Rolling T Ventures — Business Card</title>
<link href="https://fonts.googleapis.com/css2?family=Bebas+Neue&display=swap" rel="stylesheet">
<style>
  :root {
    --backdrop: #e9e6e2;
    --card-black: #0b0b0b;
    --brand-red: #e31e24;
    --ink-white: #ffffff;
    --glow-yellow: #ffd23a;
    --glow-orange: #f07a1c;
    --deep-red: #9c0d0d;
  }
  * { box-sizing: border-box; margin: 0; padding: 0; }
  html, body {
    width: 1200px; height: 1000px; overflow: hidden;
    background: var(--backdrop);
  }
  .canvas { position: relative; width: 1200px; height: 1000px; }

  .card {
    position: absolute; width: 560px; height: 320px;
    border-radius: 3px; overflow: hidden;
    box-shadow: 0 6px 18px rgba(0,0,0,.18);
  }

  /* Front */
  .card--front { left: 90px; top: 150px; background: var(--card-black); }
  .company-name {
    position: absolute; left: 0; top: 0; width: 192px; height: 320px;
    display: flex; flex-direction: column; justify-content: center; align-items: center;
    font-family: "Bebas Neue", sans-serif; font-weight: 400;
    font-size: 32px; line-height: 1.05; letter-spacing: 1px;
    color: var(--ink-white); text-align: center;
  }
  .divider {
    position: absolute; left: 192px; top: 36px; width: 2px; height: 248px;
    background: var(--ink-white);
  }
  .contact {
    position: absolute; left: 232px; top: 86px;
    font-family: "Bebas Neue", sans-serif; color: var(--ink-white);
  }
  .contact__name { font-size: 42px; font-weight: 400; letter-spacing: 1px; line-height: 1; margin-bottom: 14px; }
  .contact__initial { color: var(--brand-red); }
  .contact__list { list-style: none; }
  .contact__item {
    display: flex; align-items: center; gap: 12px;
    font-size: 19px; letter-spacing: .6px; line-height: 1; margin-bottom: 11px;
    white-space: nowrap;
  }
  .contact__item:last-child { margin-top: 6px; margin-bottom: 0; }
  .contact__icon { width: 14px; height: 14px; flex: none; }

  /* Back */
  .card--back { left: 550px; top: 530px; background: var(--card-black); }
  .lane-photo {
    position: absolute; inset: 0;
    background:
      radial-gradient(ellipse 28% 70% at 50% 78%, var(--glow-yellow) 0%, var(--glow-orange) 35%, rgba(227,30,36,.85) 60%, transparent 85%),
      linear-gradient(180deg, #151515 0%, #1c0505 40%, var(--deep-red) 70%, #120404 100%);
  }
</style>
</head>
<body>
<main class="canvas">
  <section class="card card--front" aria-label="Business card front">
    <div class="company-name">
      <span>ROLLING T</span>
      <span>VENTURES</span>
    </div>
    <div class="divider"></div>
    <div class="contact">
      <h1 class="contact__name">NEIL <span class="contact__initial">T</span> FARROW</h1>
      <ul class="contact__list">
        <li class="contact__item">
          <svg class="contact__icon" viewBox="0 0 14 14"><rect x="3" y="1" width="8" height="12" rx="1.2" fill="none" stroke="var(--brand-red)" stroke-width="1.6"/></svg>
          1-555-318-4762
        </li>
        <li class="contact__item">
          <svg class="contact__icon" viewBox="0 0 14 14"><rect x="1" y="3" width="12" height="8" fill="var(--brand-red)"/><path d="M1 3l6 4.5L13 3" fill="none" stroke="var(--card-black)" stroke-width="1"/></svg>
          NEILT@ROLLINGTVENTURES.EXAMPLE
        </li>
        <li class="contact__item">
          <svg class="contact__icon" viewBox="0 0 14 14" fill="none" stroke="var(--brand-red)" stroke-width="1.3"><circle cx="7" cy="7" r="5.8"/><ellipse cx="7" cy="7" rx="2.5" ry="5.8"/><path d="M1.2 7h11.6"/></svg>
          WWW.ROLLINGTVENTURES.EXAMPLE
        </li>
        <li class="contact__item">
          <svg class="contact__icon" viewBox="0 0 14 14"><path d="M7 13.5S2.2 8.2 2.2 5.2a4.8 4.8 0 0 1 9.6 0C11.8 8.2 7 13.5 7 13.5z" fill="var(--brand-red)"/><circle cx="7" cy="5.2" r="1.7" fill="var(--card-black)"/></svg>
          PO BOX 47, ALDER FALLS, VERMONT USA 00000
        </li>
      </ul>
    </div>
  </section>

  <section class="card card--back" aria-label="Business card back">
    <div class="lane-photo" role="img" aria-label="Photograph of a bowling lane at a tournament, pins lit in red and yellow in the foreground"></div>
  </section>
</main>
</body>
</html>
```